"Bright Hollow Craft Dwellings" need a busines Card Design got Builder

We need a business card design for a company based in Milford, Michigancalled Bright Hollow Craft Dwellings - has been recognized as a premier custom home builder. Distinguished by outstanding craftmanship and timeless beauty. Our custom home can be found in the most prestigious communities in Michigan. The homes are built with ICF (insulated concrete homes) which is green, allergy free, fire free, mold free and quitter. Our slogan "building one dream at a Time" and also we are ICF distributor for the state of Michigan

Target Market(s)

Anyone who is making over $100,000 a year and who wants to have totally custom built home. Ages from 29 up to 60 years old

Industry/Entity Type

Concrete

Contact Information for Business Card

we want to use - green, black, gray or blue colors - we want to look different with our business cards, because we built homes only with ICF, green, healthier and highly energy efficient homes.

Requirements
Must have
• I have logo that I attached and we have been using the logo (the only green home)
Nice to have
• should look quality business card,

```html
<!DOCTYPE html>
<html lang="en">
<head>
<meta charset="utf-8">
<title>Bright Hollow Craft Dwellings — Business Card</title>
<link rel="stylesheet" href="https://fonts.googleapis.com/css2?family=Montserrat:wght@400;600&family=Raleway:wght@300&family=Questrial&display=swap">
<style>
  :root {
    --stage: #2a2a2a;
    --brand-green: #9bc94a;
    --brand-green-pale: #d6eab2;
    --paper: #ffffff;
    --ink-gray: #6f6f6f;
    --tag-gray: #5e5e5e;
  }
  * { margin: 0; padding: 0; box-sizing: border-box; }
  html, body {
    width: 1200px; height: 993px; overflow: hidden;
    background: var(--stage);
  }
  .canvas { position: relative; width: 1200px; height: 993px; }

  .card {
    position: absolute; left: 280px;
    width: 640px; height: 366px; overflow: hidden;
    box-shadow: 0 8px 24px rgba(0,0,0,.45);
  }
  .card-front { top: 90px; background: var(--brand-green); color: var(--paper); }
  .card-back  { top: 537px; background: var(--paper); }

  /* Reserved area for the decorative edge motif */
  .edge-decor {
    position: absolute; top: 0; right: 0;
    width: 190px; height: 100%;
  }
  .card-front .edge-decor {
    background: linear-gradient(to right, var(--brand-green), rgba(255,255,255,.5));
  }
  .card-back .edge-decor {
    background: linear-gradient(to right, var(--paper), var(--brand-green-pale));
  }

  /* Front */
  .holder { position: absolute; left: 68px; top: 82px; font-family: "Montserrat", sans-serif; }
  .holder-name { font-size: 18px; font-weight: 600; line-height: 1.1; }
  .holder-title { font-size: 11px; font-weight: 400; margin-top: 2px; }

  .front-mark {
    position: absolute; left: 64px; top: 146px;
    width: 112px; height: 112px; border-radius: 50%;
    background: var(--paper);
  }
  .divider {
    position: absolute; left: 196px; top: 128px;
    width: 2px; height: 146px; background: var(--paper);
  }
  .contact-list {
    position: absolute; left: 216px; top: 142px; list-style: none;
    font-family: "Montserrat", sans-serif; font-size: 12px; letter-spacing: .3px;
  }
  .contact-list li { display: flex; align-items: center; height: 19px; }
  .contact-list svg { width: 11px; height: 11px; margin-right: 10px; fill: var(--paper); flex: none; }

  /* Back */
  .lockup { position: absolute; left: 78px; top: 118px; display: flex; align-items: center; }
  .lockup-dot { width: 104px; height: 104px; border-radius: 50%; background: var(--brand-green); flex: none; }
  .lockup-name {
    margin-left: 12px;
    font-family: "Raleway", sans-serif; font-weight: 300;
    font-size: 23px; line-height: 22px; letter-spacing: .5px;
    color: var(--ink-gray); text-transform: uppercase;
  }
  .tagline {
    position: absolute; left: 190px; top: 276px;
    font-family: "Questrial", sans-serif; font-size: 19px; color: var(--tag-gray);
  }
</style>
</head>
<body>
<main class="canvas">

  <section class="card card-front" aria-label="Business card front">
    <div class="edge-decor" role="img" aria-label="Decorative sunburst edge motif in white on green"></div>

    <div class="holder">
      <p class="holder-name">Marcus Hale</p>
      <p class="holder-title">General Manager</p>
    </div>

    <div class="front-mark" aria-hidden="true"></div>
    <div class="divider" aria-hidden="true"></div>

    <ul class="contact-list">
      <li><svg viewBox="0 0 24 24" aria-hidden="true"><path d="M6.6 10.8a15 15 0 0 0 6.6 6.6l2.2-2.2a1 1 0 0 1 1-.25 11.4 11.4 0 0 0 3.6.57 1 1 0 0 1 1 1V20a1 1 0 0 1-1 1A17 17 0 0 1 3 4a1 1 0 0 1 1-1h3.5a1 1 0 0 1 1 1c0 1.25.2 2.45.57 3.570a1 1 0 0 1-.25 1z"/></svg>5550-184-207 / 5550-392-615</li>
      <li><svg viewBox="0 0 24 24" aria-hidden="true"><path d="M2 5h20v14H2zM3.5 6.5 12 13l8.5-6.5z"/></svg>marcus.hale@brighthollow.com</li>
      <li><svg viewBox="0 0 24 24" aria-hidden="true"><circle cx="12" cy="12" r="10"/></svg>www.brighthollow.com</li>
      <li><svg viewBox="0 0 24 24" aria-hidden="true"><path d="M12 2a7 7 0 0 0-7 7c0 5 7 13 7 13s7-8 7-13a7 7 0 0 0-7-7zm0 9.5A2.5 2.5 0 1 1 12 6.5a2.5 2.5 0 0 1 0 5z"/></svg>Linden Ridge Road , Alder 4821</li>
    </ul>
  </section>

  <section class="card card-back" aria-label="Business card back">
    <div class="edge-decor" role="img" aria-label="Decorative sunburst edge motif in green on white"></div>

    <div class="lockup">
      <div class="lockup-dot" aria-hidden="true"></div>
      <p class="lockup-name">Bright Hollow<br>Craft Dwellings</p>
    </div>

    <p class="tagline">building one dream at a Time</p>
  </section>

</main>
</body>
</html>
```